Rate sheet redesign

We provide rate sheets to agents for our scenic flights and I would like to make them easier to read and more comprehensive. I'd also like to be able to edit the information in the design, as tours get updated and so do the rates. We've got new product out of shark bay, so the sections would need to be: Perth, Geraldton, Kalbarri and Shark Bay. I've attached what we've been using and also some concept photos.

also a link to our flights online: https://coralwingtours.bookvista.com/catalog/418752/flights-from-perth

I've put this under brochure redesign as I wasn't sure what a rate sheet would be considered. Open to different formats if it means content is editable.

Need extra days to review

```html
<!DOCTYPE html>
<html lang="en">
<head>
<meta charset="utf-8">
<title>Geraldton Rates</title>
<link href="https://fonts.googleapis.com/css2?family=Montserrat:wght@400;500;700;800&display=swap" rel="stylesheet">
<style>
  :root {
    --backdrop: #484848;
    --navy: #00579a;
    --sky: #86d4f6;
    --sky-light: #e2f5fd;
    --sky-edge: #8fd7f6;
    --logo-panel: #d6f1fc;
    --ink: #1a1a1a;
    --white: #ffffff;
    --accent: #f39a2b;
  }
  * { box-sizing: border-box; margin: 0; padding: 0; }
  html, body { width: 1200px; height: 903px; overflow: hidden; }
  body {
    background: var(--backdrop);
    font-family: "Montserrat", sans-serif;
    position: relative;
  }
  .rate-sheet {
    position: absolute;
    left: 84px; top: 87px;
    width: 1031px; height: 730px;
    background: radial-gradient(ellipse at 50% 45%, var(--sky-light) 0%, #bfe9fa 45%, var(--sky-edge) 100%);
    overflow: hidden;
  }
  .sheet-header {
    position: absolute; left: 0; top: 0;
    width: 100%; height: 168px;
    background: var(--navy);
  }
  .sheet-title {
    position: absolute; left: 50px; top: 38px;
    font-weight: 800; font-size: 58px; line-height: 1;
    color: var(--sky); letter-spacing: 0.5px;
  }
  .sheet-subtitle {
    position: absolute; left: 50px; top: 100px;
    font-weight: 700; font-size: 18.5px; line-height: 22px;
    color: var(--white);
  }
  .brand-panel {
    position: absolute; left: 780px; top: 0;
    width: 201px; height: 156px;
    background: var(--logo-panel);
    border-radius: 0 0 26px 26px;
    display: flex; flex-direction: column; align-items: center; justify-content: center; gap: 10px;
  }
  .brand-mark {
    width: 40px; height: 40px; border-radius: 50%;
    background: var(--navy);
  }
  .brand-name {
    font-weight: 700; font-size: 17px; color: var(--navy);
    text-align: center; line-height: 1.15;
  }
  .rate-table {
    position: absolute; left: 50px; top: 194px;
    display: grid;
    grid-template-columns: 225px 302px 178px 98px 93px;
    grid-template-rows: 63px 119px 119px 119px;
    column-gap: 8.5px; row-gap: 7px;
  }
  .col-head {
    background: var(--navy); color: var(--white);
    border-radius: 10px;
    display: flex; align-items: center; justify-content: center;
    font-weight: 700; font-size: 13px; letter-spacing: 0.3px;
  }
  .cell {
    background: var(--white); border-radius: 10px;
    display: flex; align-items: center; justify-content: center;
    text-align: center; color: var(--ink);
    font-size: 11.2px; line-height: 13.2px; padding: 0 14px;
  }
  .cell.clauses { padding: 0 16px; }
  .cell.price { font-weight: 500; font-size: 11.5px; padding: 0; }
  .cell p + p { margin-top: 13px; }
  .sheet-footer {
    position: absolute; left: 0; top: 660px;
    width: 100%; height: 70px;
    background: var(--navy);
    border-radius: 40px 40px 0 0;
    padding: 13px 50px 0;
    color: var(--white); font-weight: 700; font-size: 13.6px; line-height: 17px;
  }
</style>
</head>
<body>
  <main class="rate-sheet">
    <header class="sheet-header">
      <h1 class="sheet-title">GERALDTON RATES</h1>
      <p class="sheet-subtitle">TOUR RATES VALID FROM 1ST APRIL 2025 TO 31ST MARCH 2026<br>RETAIL RATES</p>
      <div class="brand-panel">
        <span class="brand-mark"></span>
        <span class="brand-name">Skyreach Aviation</span>
      </div>
    </header>

    <section class="rate-table">
      <div class="col-head">FLIGHT</div>
      <div class="col-head">INCLUSIONS</div>
      <div class="col-head">CLAUSES</div>
      <div class="col-head">ADULT</div>
      <div class="col-head">CHILD</div>

      <div class="cell flight">Abrolhos Island Discovery Tour<br>(Flight 303)</div>
      <div class="cell inclusions"><div><p>Included: Scenic flight from Geraldton to East Wallabi Island return. Morning /Afternoon Tea, and snorkel gear.</p><p>Duration: 1 hour 20 minutes flight time<br>5 hours 30 minutes Total Tour time</p></div></div>
      <div class="cell clauses">Normal departure time is 8am, however timing is flexible depending on bookings. Start time must be 6 hours before sunset.</div>
      <div class="cell price">$550.00</div>
      <div class="cell price">$385.00</div>

      <div class="cell flight">Abrolhos Island Discovery Tour<br>plus Pink Lake (Flight 304)</div>
      <div class="cell inclusions"><div><p>Included: Scenic flight from Geraldton to East Wallabi Island return via Pink Lake. Morning /Afternoon Tea, and snorkel gear.</p><p>Duration: 2 hours flight time<br>6 hours Total Tour time</p></div></div>
      <div class="cell clauses">Normal departure time is 8am, however timing is flexible depending on bookings. Start time must be 6 hours before sunset.</div>
      <div class="cell price">$610.00</div>
      <div class="cell price">$427.00</div>

      <div class="cell flight">Abrolhos Islands and Batavia<br>Shipwreck (Flight 303B)</div>
      <div class="cell inclusions"><div><p>Included: Scenic flight from Geraldton to East Wallabi Island return, and Morning /Afternoon Tea.</p><p>Duration: 1 hour 20 minutes flight time<br>2 hours Total Tour time</p></div></div>
      <div class="cell clauses">Normal departure time is 2pm, however timing is flexible depending on bookings. Start time must be 2.5 hours before sunset.</div>
      <div class="cell price">$500.00</div>
      <div class="cell price">$350.00</div>
    </section>

    <footer class="sheet-footer">
      PLEASE NOTE THERE IS A NEW $11 GOVERNMENT FEE FOR ALL FLIGHTS LANDING AT THE ABROLHOS ISLANDS, THIS IS NOT A COMMISSIONABLE FEE AND NEEDS TO BE PAID ON TOP OF THE NETT RATE
    </footer>
  </main>
</body>
</html>
```